依頼概要
本サービスの集客用FAXDMのデザインをお願い致します。

■コンセプト
「冷凍食品専門の物流倉庫!機能充実した最新設備が特長です」
※参考、物流倉庫サービスとは:https://www.kawanami-corp.jp/hokanbox/post-218

■ターゲット像:
★「冷凍食品・冷蔵食材」を扱う企業
・倉庫の確保がしたい物流会社も許容
→メーカー、卸売業者、EC業者などの区分は問わない。
→「飲食店」「食品メーカー」「農業」「卸会社」「物流会社」のリストに配布予定。

■ターゲットが保有するニーズ、あるいは課題
・品質管理のために高い冷凍機能が無いといけない。
・作業品質が悪く、納期遅延や破損・汚損が発生する。
・作業に忙殺されてしまっている。
・業績拡大に合わせて倉庫を拡張したい

■訴求するベネフィット:
①最新設備があって冷凍機能〇、その他の機能も〇。
②素晴らしい設備があるので、作業品質は万全。リソースも十分。
③埼玉県の好立地に広大な倉庫があります。首都圏にもスムーズに配送
④1個、1パレット、1日の小規模案件も喜んでご対応
⑤特定の期間のみ発送を強化してほしいなど柔軟に対応します。
→「衝撃のプライス!」のように価格を強く訴求することも可
→入庫料は無料

■その他、参考表現:
・埼玉県加須市に冷凍倉庫が出来ました
・保管商品を大募集しています
・1日からでも使えます
・費用は格安、保管費用は1パレット1日40円~(税込44円)から
(※パレットとは縦110cm×横110cmの保管単位です)
・ピッキングや発送業務も承ります

■必須の項目:
・相手の社名、担当者名、電話番号、メールアドレスを書く欄
・問い合わせ先として「受付センターの電話番号とFAX番号」を記載
TEL:0120-731-904/FAX:0280-47-9163
グリーンウェーブ受付センター 埼玉県加須市松葉912
受付時間9:00~18:00(日・3が日除く)

幅広く複数案の採用を考えています。
参考資料として、これまでのFAXDMデザインをお送り致します。

以上です。
■ 選んだ理由

弊社の雰囲気に合ったデザインを選ばせていただきました。FAXDM用ですので小さい字ではなく大きな字でわかりやすいデザインが良かったです。

■ 提案者全員のお礼・コメント

ありがとうございました。次回の制作予定ががありましたら積極的に本サイトを利用させていただきます。

```html
<!DOCTYPE html>
<html lang="ja">
<head>
<meta charset="utf-8">
<title>冷凍倉庫 保管商品大募集 FAXDM</title>
<link rel="stylesheet" href="https://fonts.googleapis.com/css2?family=Noto+Sans+JP:wght@400;500;700;900&display=swap">
<style>
:root{
  --ink:#111111;
  --paper:#ffffff;
  --mid:#8a8a8a;
  --light:#d9d9d9;
  --line:#222222;
}
*{margin:0;padding:0;box-sizing:border-box}
html,body{width:846px;height:1200px;overflow:hidden;background:var(--paper)}
body{font-family:"Noto Sans JP",sans-serif;color:var(--ink);position:relative}
.abs{position:absolute}

.headline{left:0;top:18px;width:846px;text-align:center;font-weight:900;font-size:44px;letter-spacing:1px;line-height:62px;white-space:nowrap}
.headline .hl{background:var(--ink);color:var(--paper);padding:0 10px;margin:0 4px;display:inline-block}
.subline{left:0;top:96px;width:846px;text-align:center;font-weight:900;font-size:31px;white-space:nowrap}

.banner{left:22px;top:148px;width:802px;height:84px;background:var(--ink);color:var(--paper);font-weight:900;font-size:66px;text-align:center;line-height:84px;letter-spacing:4px}

.shock{left:22px;top:252px;width:170px;height:116px;background:var(--ink);color:var(--paper);border-radius:18px;transform:rotate(-10deg);font-weight:900;font-size:40px;line-height:48px;text-align:center;padding-top:10px}
.pallet-note{left:214px;top:360px;font-size:12px;font-weight:500;white-space:nowrap}
.building{left:36px;top:395px;width:440px;height:160px;background:linear-gradient(180deg,var(--light),var(--mid));border-bottom:6px solid var(--ink)}

.fee-label{left:462px;top:258px;width:150px;height:46px;border:4px solid var(--ink);font-weight:900;font-size:28px;text-align:center;line-height:38px;white-space:nowrap}
.fee-unit{left:626px;top:254px;font-weight:900;font-size:34px;line-height:54px;white-space:nowrap;letter-spacing:-1px}
.free{left:466px;top:314px;font-weight:700;font-size:21px;white-space:nowrap}
.price{left:478px;top:340px;font-weight:900;font-size:210px;line-height:210px;letter-spacing:-6px}
.yen{left:712px;top:440px;font-weight:900;font-size:74px;line-height:80px;white-space:nowrap}
.yen small{font-size:28px}
.tax{left:728px;top:524px;font-size:18px;font-weight:700;white-space:nowrap}

.sectors{left:0;top:570px;width:846px;text-align:center;font-weight:900;font-size:23px;border-top:3px solid var(--ink);padding-top:10px;white-space:nowrap}

.features{left:28px;top:618px;width:790px;display:grid;grid-template-columns:repeat(3,1fr);gap:14px}
.feature{border:3px solid var(--ink);border-radius:16px;height:98px;display:flex;align-items:center;padding:0 12px;font-weight:700;font-size:18px;line-height:28px;white-space:nowrap}

.ask{left:30px;top:850px;font-weight:900;font-size:24px;line-height:32px;white-space:nowrap}
.fax-badge{left:262px;top:846px;width:92px;height:72px;background:var(--ink);color:var(--paper);border-radius:36px;display:flex;flex-direction:column;align-items:center;justify-content:center;font-weight:700;font-size:15px;line-height:19px}
.fax-number{left:368px;top:838px;font-weight:900;font-size:60px;line-height:80px;white-space:nowrap}
.fax-note{left:370px;top:918px;width:450px;font-size:12px;font-weight:500;line-height:17px}

.form{left:28px;top:960px;width:790px;border-collapse:collapse;table-layout:fixed}
.form td{border:2px solid var(--line);height:64px;vertical-align:top;font-size:19px;font-weight:700;padding:6px 10px}
.form .label{width:112px;text-align:center;vertical-align:middle}
.form .ruby{font-size:11px;font-weight:400;display:block;border-bottom:1px dashed var(--mid);height:18px}

.footer{left:22px;top:1108px;width:802px;height:78px;border:3px solid var(--ink);display:flex;align-items:center}
.call-badge{width:92px;height:72px;background:var(--ink);color:var(--paper);display:flex;flex-direction:column;align-items:center;justify-content:center;font-size:14px;font-weight:700;line-height:19px}
.center-info{padding-left:16px;width:320px}
.center-name{font-weight:900;font-size:21px;white-space:nowrap}
.center-addr{font-size:15px;font-weight:500;text-align:right}
.tel-block{flex:1;padding-left:10px}
.tel{display:flex;align-items:center;gap:8px;font-weight:900;font-size:42px;line-height:48px;white-space:nowrap}
.hours{font-size:12px;font-weight:500;padding-left:52px;white-space:nowrap}
</style>
</head>
<body>

<h1 class="abs headline">埼玉県加須市に<span class="hl">冷凍倉庫</span>が出来ました。</h1>
<p class="abs subline">冷凍食品専門の物流倉庫！ 機能充実した最新設備</p>

<div class="abs banner">保管商品大募集!!</div>

<div class="abs shock">衝撃の<br>価格!</div>
<p class="abs pallet-note">※パレットとは縦110cm×横110cmの保管単位です</p>
<div class="abs building" role="img" aria-label="雪の結晶に囲まれた冷凍倉庫の建物のイラスト"></div>

<div class="abs fee-label">保管費用</div>
<div class="abs fee-unit">1パレット1日</div>
<div class="abs free">▲入庫料は無料</div>
<div class="abs price">40</div>
<div class="abs yen">円<small>から</small></div>
<div class="abs tax">(税込44円)</div>

<p class="abs sectors">その他、メーカー・卸売業者・EC業者など様々な業種に対応しております。</p>

<div class="abs features">
  <div class="feature">最新設備で冷凍機能、<br>その他の機能も万全。</div>
  <div class="feature">最新設備で作業品質は<br>万全。リソースも十分。</div>
  <div class="feature">好立地な場所で、首都圏<br>にもスムーズに配送。</div>
  <div class="feature">1個、1パレット、1日の<br>小規模案件も対応可。</div>
  <div class="feature">特定の期間のみ発送強化<br>なども柔軟に対応します。</div>
  <div class="feature">その他、ピッキングや<br>発送業務も承ります。</div>
</div>

<p class="abs ask">FAXもしくは<br>お電話にてお気軽に<br>お問い合わせ下さい。</p>
<div class="abs fax-badge">FAXでの<br>問い合わせ</div>
<div class="abs fax-number">0280-47-9163</div>
<p class="abs fax-note">※FAXでお問い合わせの場合は、記入欄に記入の上、上記FAX番号に送信してください。後日、担当者よりご連絡いたします。</p>

<table class="abs form">
  <tr>
    <td class="label">貴 社 名</td>
    <td><span class="ruby">フリガナ</span></td>
    <td class="label">担当者名</td>
    <td><span class="ruby">フリガナ</span></td>
  </tr>
  <tr>
    <td class="label">電話番号</td>
    <td></td>
    <td class="label">メール<br>アドレス</td>
    <td></td>
  </tr>
</table>

<div class="abs footer">
  <div class="call-badge">お電話での<br>問い合わせ</div>
  <div class="center-info">
    <div class="center-name">グリーンウェーブ受付センター</div>
    <div class="center-addr">埼玉県加須市松葉912</div>
  </div>
  <div class="tel-block">
    <div class="tel">
      <svg width="38" height="38" viewBox="0 0 24 24" aria-hidden="true"><path fill="#111" d="M6.6 10.8a15.1 15.1 0 0 0 6.6 6.6l2.2-2.2a1 1 0 0 1 1-.25 11.4 11.4 0 0 0 3.6.57 1 1 0 0 1 1 1V20a1 1 0 0 1-1 1A17 17 0 0 1 3 4a1 1 0 0 1 1-1h3.5a1 1 0 0 1 1 1c0 1.25.2 2.45.57 3.57a1 1 0 0 1-.25 1z"/></svg>
      0120-731-904
    </div>
    <div class="hours">受付時間 9:00～18:00（日・3が日除く）</div>
  </div>
</div>

</body>
</html>
```